wardrobe/costume stylist needs good business card for own business

Hi:)

I'm wanting a business card for my company. I am a freelance stylist.

I do wardrobe/costume stylist to TV commercials; Films; Fashion and Lifestyle shoots.

I'd like a design based around my name Rosalind Pember written nicely, maybe a colour? Up to you?!

I've attached a couple of images of business cards I like
.... be creative and have fun!

Thank you :)
Updates

Reason: I was trying to get my new business card ready for before I headed overseas Friday morning but I don't think that was realistic so I'd like to extend the deadline to give time to the project. Thank you

Hi designers:) Thank you for all your designs, I've extended the deadline until Sunday, so there's a bit more time. I've attached 3 pictures of business cards which I quite like, please take a look to see if it can be of help in your process. I like the pale plain or patterned background with dark font and the dark plain or patterned background with the pale font the motifs the feminine fonts the plain fonts I like the idea of playing with a circle or some shape on one side of the card with my name or initials as in the picture I have on my post could you play around with this idea a bit please? Thank you all for the work you've done :) Rosa

Hi I am working overseas til Saturday night sorry for no feedback until I teturn Thanks :) Rosa

Hi designers, Thank you all so much for submitting your designs, I really appreciate your input into my project :) I'm sorry I didn't get to respond to some comments, and give feedback. I didn't back from being away until later than I expected, and the deadline had passed then, so apologies. Thanks to you all again for all your really good designs :) Rosa

Target Market(s)

I am a freelance stylist my target audience is producers, production companies, photographers, directors...

Industry/Entity Type

Business

Requirements
Must have
• Rosalind Pember
Stylist or Wardrobe Stylist

email rosapember@quillnet.co.nz
Mobile 0218846193

(Don't have to use the words 'email' and 'mobile')
Nice to have
• Would like it to be double sided
Like B & W
Like pale colour background with dark font or white font
Like dark colour background with pale font
Should not have
• I would prefer it not to incorporate pictures

```html
<!DOCTYPE html>
<html lang="en">
<head>
<meta charset="utf-8">
<title>Rosalind Pember – Wardrobe Stylist Business Card</title>
<link href="https://fonts.googleapis.com/css2?family=Jost:wght@400;600&display=swap" rel="stylesheet">
<style>
  :root {
    --backdrop: #1e1e1e;
    --card-white: #ffffff;
    --brand-pink: #c01f50;
    --ink-dark: #333333;
    --ink-light: #ffffff;
  }
  * { margin: 0; padding: 0; box-sizing: border-box; }
  html, body {
    width: 1200px;
    height: 1000px;
    overflow: hidden;
    background: var(--backdrop);
    font-family: "Jost", sans-serif;
  }
  .stage { position: relative; width: 1200px; height: 1000px; }
  .card {
    position: absolute;
    left: 197px;
    width: 787px;
    height: 461px;
    box-shadow: 0 6px 10px rgba(0, 0, 0, 0.45);
  }
  .card--front { top: 33px; background: var(--card-white); }
  .card--back { top: 513px; background: var(--brand-pink); color: var(--ink-light); }

  .front-name {
    position: absolute;
    left: 99px;
    top: 178px;
    width: 586px;
    text-align: center;
    font-weight: 600;
    font-size: 50px;
    letter-spacing: 0.04em;
    color: var(--brand-pink);
    line-height: 1;
  }
  .front-title {
    position: absolute;
    left: 103px;
    top: 258px;
    width: 600px;
    font-weight: 400;
    font-size: 34px;
    letter-spacing: 0.47em;
    color: var(--ink-dark);
    line-height: 1;
    white-space: nowrap;
  }

  .back-brand {
    position: absolute;
    left: 88px;
    top: 160px;
    width: 230px;
    font-weight: 600;
    font-size: 40px;
    line-height: 1.05;
    letter-spacing: 0.03em;
    color: var(--ink-light);
  }
  .back-divider {
    position: absolute;
    left: 370px;
    top: 142px;
    width: 3px;
    height: 168px;
    background: var(--ink-light);
  }
  .back-details { position: absolute; left: 408px; top: 138px; }
  .back-name { font-size: 29px; font-weight: 400; line-height: 1; letter-spacing: 0.01em; }
  .back-role { font-size: 20px; font-weight: 400; margin-top: 10px; line-height: 1; }
  .contact-list { list-style: none; margin-top: 55px; }
  .contact-item {
    display: flex;
    align-items: center;
    gap: 12px;
    font-size: 20px;
    line-height: 1;
    height: 24px;
    margin-bottom: 13px;
  }
  .contact-icon { width: 18px; height: 22px; flex: none; }
</style>
</head>
<body>
  <main class="stage">
    <section class="card card--front" aria-label="Card front">
      <h1 class="front-name">ROSALIND PEMBER</h1>
      <p class="front-title">WARDROBE STYLIST</p>
    </section>

    <section class="card card--back" aria-label="Card back">
      <p class="back-brand">ROSALIND<br>PEMBER</p>
      <div class="back-divider"></div>
      <div class="back-details">
        <h2 class="back-name">ROSALIND PEMBER</h2>
        <p class="back-role">Wardrobe Stylist</p>
        <ul class="contact-list">
          <li class="contact-item">
            <svg class="contact-icon" viewBox="0 0 18 22" aria-hidden="true">
              <rect x="3" y="1" width="12" height="20" rx="2" fill="none" stroke="#fff" stroke-width="2"/>
              <rect x="7" y="17" width="4" height="1.6" fill="#fff"/>
            </svg>
            <span>0218846193</span>
          </li>
          <li class="contact-item">
            <svg class="contact-icon" viewBox="0 0 20 22" aria-hidden="true">
              <rect x="0" y="6" width="20" height="13" fill="#fff"/>
              <path d="M0 6 L10 13 L20 6" fill="none" stroke="#c01f50" stroke-width="1.6"/>
            </svg>
            <span>rosapember@quillnet.co.nz</span>
          </li>
        </ul>
      </div>
    </section>
  </main>
</body>
</html>
```